Dane Morrow films- wedding and event films company website. DESKTOP AND MOBILE

We need a website for a high-end wedding and event film production company. Looking for a very modern and elegant design. my old website is www.danemorrowfilms.example

I like the "white/black/rose gold" color scheme of my logo.

really looking for a sleek modern design the breaths professional and artistic.

Target Market(s)

wedding and event films.

Industry/Entity Type

Film Production

Number of Pages Required

5+ page

Colors

Designer to choose colors to be used in the design.

Requirements
Must have
• website name will be www.danemorrowfilms.example
• tagline is "CINEMATIC STORIES ABOUT YOU"
• sections: HOME, CONTACT, ABOUT, FILMS, BLOG
• You can see my old website at danemorrowfilms.example
• Website about section:
• Dane Morrow Films was Established with the basis of truly cinematic and artistic films in mind. Dane and his team routinely travel the globe documenting weddings and events for high profile clients and discerning couples. Dane was born and raised in Maui Hawaii and has a unique approach to his films that embody the essence of a Hollywood film. Dane has spent the last 10 years traveling the world documenting corporate events and weddings with multiple Award winning production companies. In 2017 Dane decided to establish his own brand “Dane Morrow films” that will take everything he has learned with his past experiences and push it to the next level. Aside from his personal achievements, Dane is extremely passionate about his craft and always looks forward to handcrafting beautiful wedding/event films for his clients. The style of work is non-traditional and the day of filming is extremely unobtrusive (as we are looking for natural-candid/ raw emotions).
• If you are looking for the best price in town, we are probably not the best option, but if you’re looking for the best quality and peace of mind on your wedding day, then you’re in the right place. Dane Morrow Films is a boutique studio that only accepts a limited number of assignments per year. Inquire early to ensure availability.
• LINKS TO VIMEO VIDEOS THAT WILL BE IN THE "FILMS' SECTION.
• BRENT FILM TRAILER - https://clipvault.example/508114362
• BRENT FEATURE FILM - https://clipvault.example/617392048
• JUNE AND ROB'S WEDDING - https://clipvault.example/724958160
• DRONE DEMO REEL - https://clipvault.example/841576203
• WEDDING INDUSTRY EVENT PARTY - https://clipvault.example/962304817/a8d3e7b21c
• images that you can use on site are here: https://brigittolsenimages.proofbox.example/gallery/nora&felix/
• password is: meadow

```html
<!DOCTYPE html>
<html lang="en">
<head>
<meta charset="utf-8">
<title>Dane Morrow Films — Cinematic Stories About You</title>
<link rel="stylesheet" href="https://fonts.googleapis.com/css2?family=Montserrat:wght@400;500;600;700;800&display=swap">
<style>
:root{
  --ink:#ffffff;
  --ink-soft:#c9c9c9;
  --ink-mute:#8d8d8d;
  --bg:#151515;
  --bg-2:#1d1d1d;
  --panel:#262626;
  --panel-line:#3a3a3a;
  --accent:#e59a5c;
  --accent-deep:#c97a3c;
  --field:#ffffff;
}
*{box-sizing:border-box;margin:0;padding:0}
html,body{width:1200px;height:4337px;overflow:hidden;background:var(--bg);font-family:"Montserrat",Arial,sans-serif;color:var(--ink)}
.page{position:relative;width:1200px;height:4337px;overflow:hidden}
section,header{position:absolute;left:0;width:1200px;overflow:hidden}
.fill{position:absolute;inset:0}

/* header + hero */
.hero{top:0;height:599px}
.hero .fill{background:radial-gradient(ellipse at 30% 70%,#6b5a45 0%,#3a3128 35%,#1b1815 80%),#1b1815}
.hero .shade{position:absolute;inset:0;background:linear-gradient(180deg,rgba(0,0,0,.55) 0%,rgba(0,0,0,.25) 40%,rgba(0,0,0,.55) 100%)}
.nav{position:absolute;top:0;left:0;width:1200px;height:98px;background:rgba(0,0,0,.55)}
.brand{position:absolute;left:173px;top:34px;display:flex;align-items:center;gap:10px;font-size:17px;font-weight:600;color:var(--ink);letter-spacing:1px;text-transform:uppercase}
.brand i{width:14px;height:14px;border-radius:50%;background:var(--accent);display:block}
.menu{position:absolute;left:471px;top:40px;display:flex;gap:34px;font-size:14px;font-weight:600;letter-spacing:.5px}
.menu a{color:var(--ink);text-decoration:none;padding-bottom:8px}
.menu a.active{border-bottom:2px solid var(--ink)}
.nav-phone{position:absolute;left:905px;top:40px;font-size:15px;font-weight:600;color:var(--accent);display:flex;align-items:center;gap:8px}
.tagline{position:absolute;top:268px;left:0;width:1200px;text-align:center;font-size:56px;font-weight:800;line-height:56px;letter-spacing:1px;text-shadow:0 2px 10px rgba(0,0,0,.5)}
.arrow{position:absolute;top:318px}

/* films + services */
.showcase{top:599px;height:1359px}
.showcase .fill{background:radial-gradient(ellipse at 50% 45%,#3a3634 0%,#1f1d1c 45%,#141414 80%)}
.section-title{position:absolute;left:0;width:1200px;text-align:center;font-size:32px;font-weight:700}
.thumb{position:absolute;top:147px;width:270px;height:180px;border-radius:3px;overflow:hidden}
.thumb .bar{position:absolute;left:0;bottom:0;width:100%;height:30px;background:rgba(0,0,0,.75)}
.thumb .bar b{position:absolute;left:34px;top:13px;width:150px;height:4px;background:#9fb4c2}
.thumb .bar em{position:absolute;left:34px;top:13px;width:50px;height:4px;background:#1fa7e0}
.thumb .bar svg{position:absolute;left:10px;top:8px}
.thumb .side{position:absolute;right:8px;top:8px;width:22px;height:60px;display:flex;flex-direction:column;gap:6px}
.thumb .side span{display:block;height:16px;background:rgba(0,0,0,.7);border-radius:2px}
.btn{position:absolute;height:38px;border:2px solid #8a8a8a;border-radius:20px;font-size:13px;font-weight:600;display:flex;align-items:center;justify-content:center;color:var(--ink)}
.service{position:absolute;width:280px;text-align:center}
.service .ring{margin:0 auto;width:176px;height:176px;border-radius:50%;background:radial-gradient(circle,#2a2a2a 0 58%,var(--accent) 58% 66%,#1c1c1c 66% 100%);box-shadow:0 0 30px rgba(0,0,0,.7);display:flex;align-items:center;justify-content:center}
.service h3{margin-top:38px;font-size:19px;font-weight:700}
.service p{margin-top:14px;font-size:13px;line-height:20px;color:var(--ink-mute)}

/* philosophy */
.philosophy{top:1958px;height:341px}
.philosophy .fill{background:linear-gradient(90deg,#6b5b4c 0%,#b89a80 30%,#8f7866 55%,#5d564c 80%,#3b3a36 100%)}
.philosophy .shade{position:absolute;inset:0;background:rgba(0,0,0,.25)}
.philosophy h2{position:absolute;top:106px;width:1200px;text-align:center;font-size:32px;font-weight:700}
.philosophy p{position:absolute;top:160px;left:280px;width:640px;text-align:center;font-size:18px;font-weight:700;line-height:28px}

/* packages */
.packages{top:2299px;height:983px}
.packages .fill{background:linear-gradient(90deg,#141414 0%,#1a1a1a 55%,#3a3a3a 85%,#262626 100%)}
.card{position:absolute;top:150px;width:388px;height:755px;background:rgba(28,28,28,.92)}
.card.standard{left:202px;border:3px solid #4a4a4a}
.card.complete{left:610px;border:3px solid var(--accent)}
.card header{position:relative;height:64px;display:flex;align-items:center;justify-content:center;font-size:18px;font-weight:700;width:100%}
.standard header{background:#3b3b3b}
.complete header{background:var(--accent)}
.card ul{list-style:none;padding:0 30px}
.card li{height:57px;border-bottom:1px solid var(--panel-line);display:flex;align-items:center;justify-content:center;text-align:center;font-size:13px;line-height:18px;color:var(--ink-soft)}
.card li strong{color:var(--ink);font-weight:700}
.card li.price{color:var(--accent);font-weight:700;font-size:14px}
.card li.note{border-bottom:none;color:var(--ink);font-weight:700;height:72px}

/* gallery */
.gallery{top:3282px;height:347px}
.gallery .fill{background:linear-gradient(90deg,#2f3a22 0%,#4d5a34 30%,#6b6a55 55%,#3b4a2a 80%,#25301b 100%)}
.gallery .shade{position:absolute;inset:0;background:rgba(0,0,0,.3)}
.gallery h2{position:absolute;top:98px;width:1200px;text-align:center;font-size:32px;font-weight:700}
.gallery p{position:absolute;top:152px;width:1200px;text-align:center;font-size:18px;font-weight:700}
.btn.accent{border-color:var(--accent);background:rgba(0,0,0,.45)}

/* contact */
.contact{top:3629px;height:708px}
.contact .fill{background:radial-gradient(ellipse at 60% 30%,#2a2826 0%,#161616 60%,#111 100%)}
.contact h2{position:absolute;top:67px;width:1200px;text-align:center;font-size:32px;font-weight:700}
.contact .sub{position:absolute;top:122px;width:1200px;text-align:center;font-size:18px;font-weight:700}
.contact-brand{position:absolute;left:173px;top:215px;display:flex;align-items:center;gap:10px;font-size:16px;font-weight:600;text-transform:uppercase;letter-spacing:1px}
.contact-brand i{width:14px;height:14px;border-radius:50%;background:var(--accent);display:block}
.info{position:absolute;left:173px;display:flex;gap:18px;font-size:13px;line-height:18px;color:var(--ink-soft)}
.info .dot{width:34px;height:34px;border-radius:50%;background:var(--accent);flex:none;display:flex;align-items:center;justify-content:center}
.info strong{color:var(--accent);font-weight:700}
.field{position:absolute;height:37px;background:var(--field);font-size:11px;color:#8a8a8a;padding:10px 10px}
.submit{position:absolute;left:480px;top:419px;width:547px;height:35px;background:var(--accent);font-size:14px;font-weight:700;display:flex;align-items:center;justify-content:center}
.legal{position:absolute;top:580px;width:1200px;text-align:center;font-size:12px;line-height:20px;color:var(--ink-mute)}
.social{position:absolute;top:635px;left:0;width:1200px;display:flex;justify-content:center;gap:8px}
.social span{width:30px;height:30px;border-radius:50%;border:2px solid #7a7a7a;display:block}
</style>
</head>
<body>
<div class="page">

<section class="hero">
  <div class="fill" role="img" aria-label="Evening wedding reception on a lantern-lit terrace with guests at tables"></div>
  <div class="shade"></div>
  <div class="nav">
    <div class="brand"><i></i>Dane Morrow Films</div>
    <nav class="menu">
      <a class="active">HOME</a><a>ABOUT</a><a>FILMS</a><a>BLOG</a><a>CONTACT</a>
    </nav>
    <div class="nav-phone">
      <svg width="16" height="16" viewBox="0 0 24 24"><path fill="#e59a5c" d="M6.6 10.8a15 15 0 0 0 6.6 6.6l2.2-2.2c.3-.3.7-.4 1-.2 1.1.4 2.3.6 3.6.6.6 0 1 .4 1 1V20c0 .6-.4 1-1 1A17 17 0 0 1 3 4c0-.6.4-1 1-1h3.5c.6 0 1 .4 1 1 0 1.3.2 2.5.6 3.6.1.3 0 .7-.2 1z"/></svg>
      1800 555 0142
    </div>
  </div>
  <h1 class="tagline">CINEMATIC STORIES<br>ABOUT YOU</h1>
  <svg class="arrow" style="left:66px" width="30" height="30" viewBox="0 0 30 30"><path d="M20 4 9 15l11 11" stroke="#fff" stroke-width="3" fill="none"/></svg>
  <svg class="arrow" style="left:1104px" width="30" height="30" viewBox="0 0 30 30"><path d="M10 4l11 11-11 11" stroke="#fff" stroke-width="3" fill="none"/></svg>
</section>

<section class="showcase">
  <div class="fill" role="img" aria-label="Faint dark backdrop of a couple dancing"></div>
  <h2 class="section-title" style="top:66px">Our Highlight Films</h2>

  <div class="thumb" style="left:173px">
    <div class="fill" role="img" aria-label="Aerial view of a coastal town and turquoise sea" style="background:linear-gradient(180deg,#8fb6c4 0%,#5f9fb0 40%,#2f7b8c 70%,#4b6b5a 100%)"></div>
    <div class="side"><span></span><span></span><span></span></div>
    <div class="bar"><svg width="16" height="16"><path d="M3 2l11 6-11 6z" fill="#fff"/></svg><b></b><em></em></div>
  </div>
  <div class="thumb" style="left:466px">
    <div class="fill" role="img" aria-label="Bride and groom standing on a bright terrace" style="background:linear-gradient(90deg,#d9d6cf 0%,#b9b6ae 40%,#e8e6e1 70%,#a8a49c 100%)"></div>
    <div class="side"><span></span><span></span><span></span></div>
    <div class="bar"><svg width="16" height="16"><path d="M3 2l11 6-11 6z" fill="#fff"/></svg><b></b><em></em></div>
  </div>
  <div class="thumb" style="left:758px">
    <div class="fill" role="img" aria-label="Wedding guests celebrating together" style="background:linear-gradient(90deg,#6d5a45 0%,#a98e70 45%,#7a6a55 75%,#4e4337 100%)"></div>
    <div class="side"><span></span><span></span><span></span></div>
    <div class="bar"><svg width="16" height="16"><path d="M3 2l11 6-11 6z" fill="#fff"/></svg><b></b><em></em></div>
  </div>

  <div class="btn" style="left:510px;top:362px;width:180px">Explore More Films</div>

  <h2 class="section-title" style="top:545px">Production Services</h2>

  <div class="service" style="left:169px;top:620px">
    <div class="ring"><svg width="56" height="56" viewBox="0 0 56 56" fill="none" stroke="#fff" stroke-width="3"><rect x="8" y="8" width="40" height="40" rx="2"/><path d="M18 8v40M38 8v40M8 18h10M8 28h10M8 38h10M38 18h10M38 28h10M38 38h10"/></svg></div>
    <h3>Cinematic Production</h3>
    <p>Nullam ac urna eu felis dapibus<br>condimentum sit amet a augue sed non<br>condimentum fermentum nunc.</p>
  </div>
  <div class="service" style="left:459px;top:620px">
    <div class="ring"><svg width="60" height="56" viewBox="0 0 60 56" fill="none" stroke="#fff" stroke-width="3"><path d="M6 10h14M40 10h14M13 10v6M47 10v6"/><rect x="18" y="18" width="24" height="16" rx="3"/><path d="M13 16l5 6M47 16l-5 6M22 34l-4 8M38 34l4 8"/><circle cx="30" cy="40" r="4"/></svg></div>
    <h3>Aerial Drones</h3>
    <p>Nullam ac urna eu felis dapibus<br>condimentum sit amet a augue sed non<br>condimentum fermentum nunc.</p>
  </div>
  <div class="service" style="left:751px;top:620px">
    <div class="ring"><svg width="56" height="56" viewBox="0 0 56 56" fill="none" stroke="#fff" stroke-width="3"><circle cx="28" cy="28" r="20"/><path d="M28 16v12h10"/></svg></div>
    <h3>Time Lapse</h3>
    <p>Nullam ac urna eu felis dapibus<br>condimentum sit amet a augue sed non<br>condimentum fermentum nunc.</p>
  </div>

  <div class="service" style="left:169px;top:981px">
    <div class="ring"><svg width="60" height="56" viewBox="0 0 60 56"><circle cx="18" cy="16" r="8" fill="#fff"/><circle cx="36" cy="16" r="8" fill="#fff"/><rect x="8" y="26" width="34" height="20" rx="2" fill="#fff"/><path d="M42 32l12-6v20l-12-6z" fill="#fff"/></svg></div>
    <h3>Lighting and Sound</h3>
    <p>Nullam ac urna eu felis dapibus<br>condimentum sit amet a augue sed non<br>condimentum fermentum nunc.</p>
  </div>
  <div class="service" style="left:459px;top:981px">
    <div class="ring"><svg width="56" height="56" viewBox="0 0 56 56" fill="none" stroke="#fff" stroke-width="3"><rect x="8" y="10" width="40" height="36" rx="2"/><path d="M12 42l12-14 8 9 6-6 8 11"/><circle cx="36" cy="20" r="3"/></svg></div>
    <h3>Motion Graphics</h3>
    <p>Nullam ac urna eu felis dapibus<br>condimentum sit amet a augue sed non<br>condimentum fermentum nunc.</p>
  </div>
  <div class="service" style="left:751px;top:981px">
    <div class="ring"><svg width="56" height="56" viewBox="0 0 56 56" fill="none" stroke="#fff" stroke-width="3"><rect x="6" y="10" width="44" height="28" rx="2"/><path d="M22 46h12M28 38v8"/></svg></div>
    <h3>Post Production</h3>
    <p>Nullam ac urna eu felis dapibus<br>condimentum sit amet a augue sed non<br>condimentum fermentum nunc.</p>
  </div>
</section>

<section class="philosophy">
  <div class="fill" role="img" aria-label="Bride and groom embracing while a videographer films the reception"></div>
  <div class="shade"></div>
  <h2>Our Philosophy</h2>
  <p>Our goal is to provide excellent cinematic videography service to you based on your unique needs and wishes.</p>
</section>

<section class="packages">
  <div class="fill" role="img" aria-label="Dark backdrop with wedding guests in monochrome on the right"></div>
  <h2 class="section-title" style="top:74px">All Inclusive Packages</h2>

  <div class="card standard">
    <header>Our Standard Package</header>
    <ul>
      <li><span>Extended length <strong>Highlight Film</strong> (15-18 minutes)</span></li>
      <li><span><strong>Full Length Documentary Style Version</strong><br>(3 to 4 hours)</span></li>
      <li><span>Up to 13 Hours contiguous coverage</span></li>
      <li><span><strong>Filming begins at ceremony location</strong> up to 2<br>hours before ceremony</span></li>
      <li><span><strong>Two Videographers</strong> for ceremony and<br>reception coverage</span></li>
      <li><span><strong>Creative filming</strong> at park/photo locations</span></li>
      <li><span><strong>Two videographer</strong> coverage of main<br>reception events</span></li>
      <li><span><strong>Plenty of footage</strong> of dancing and reception fun!</span></li>
      <li><span><strong>Online posting</strong> of HD highlight movie (if desired)</span></li>
      <li><span>Final copies available on Flash Drive or<br>HD Blu-ray discs</span></li>
      <li class="price">$2,000 plus sales tax if applicable</li>
      <li class="note"><span>Package may be customized to fit your needs<br>extra fees may apply</span></li>
    </ul>
  </div>

  <div class="card complete">
    <header>Our Complete Package</header>
    <ul>
      <li><span>Extended length <strong>Highlight Film</strong> (15-18 minutes)</span></li>
      <li><span><strong>Full Length Documentary Style Version</strong><br>(3 to 4 hours)</span></li>
      <li><span>Up to <strong>13 Hours</strong> contiguous coverage</span></li>
      <li><span><strong>Getting Ready Footage</strong> at salon, house or hotel<br>up to 3 hours prior to wedding</span></li>
      <li><span><strong>Two Videographers</strong> for ceremony and<br>reception coverage</span></li>
      <li><span><strong>Creative filming</strong> at park/photo locations</span></li>
      <li><span><strong>Two videographer</strong> coverage of main<br>reception events</span></li>
      <li><span><strong>Plenty of footage</strong> of dancing and reception fun!</span></li>
      <li><span><strong>Online posting</strong> of HD highlight movie (if desired)</span></li>
      <li><span>Final copies available on Flash Drive or<br>HD Blu-ray discs</span></li>
      <li class="price">$2,300 plus sales tax if applicable</li>
      <li class="note"><span>Package may be customized to fit your needs<br>extra fees may apply</span></li>
    </ul>
  </div>
</section>

<section class="gallery">
  <div class="fill" role="img" aria-label="Bride and groom outdoors in a sunlit garden"></div>
  <div class="shade"></div>
  <h2>A few of our favorite recent projects</h2>
  <p>click the button to see our full gallery!</p>
  <div class="btn accent" style="left:510px;top:209px;width:180px">Explore Our Gallery</div>
</section>

<section class="contact">
  <div class="fill" role="img" aria-label="Dark faded backdrop of a wedding couple"></div>
  <h2>We would love to be part of your big day!</h2>
  <p class="sub">please contact us today</p>

  <div class="contact-brand"><i></i>Dane Morrow Films</div>

  <div class="info" style="top:297px">
    <span class="dot"><svg width="16" height="18" viewBox="0 0 24 24"><path fill="#fff" d="M12 2a7 7 0 0 0-7 7c0 5 7 13 7 13s7-8 7-13a7 7 0 0 0-7-7zm0 9.5A2.5 2.5 0 1 1 12 6.5a2.5 2.5 0 0 1 0 5z"/></svg></span>
    <span>Dane Morrow Films<br>228, Lorem Ipsum dolor,<br>dolor amet sit 84595</span>
  </div>
  <div class="info" style="top:372px">
    <span class="dot"><svg width="16" height="16" viewBox="0 0 24 24"><path fill="#fff" d="M6.6 10.8a15 15 0 0 0 6.6 6.6l2.2-2.2c.3-.3.7-.4 1-.2 1.1.4 2.3.6 3.6.6.6 0 1 .4 1 1V20c0 .6-.4 1-1 1A17 17 0 0 1 3 4c0-.6.4-1 1-1h3.5c.6 0 1 .4 1 1 0 1.3.2 2.5.6 3.6.1.3 0 .7-.2 1z"/></svg></span>
    <span>Call Us<br><strong>1800 555 0142</strong></span>
  </div>
  <div class="info" style="top:437px">
    <span class="dot"><svg width="16" height="14" viewBox="0 0 24 20"><rect x="1" y="2" width="22" height="16" rx="2" fill="#fff"/><path d="M2 3l10 8 10-8" stroke="#e59a5c" stroke-width="2" fill="none"/></svg></span>
    <span>Email Us<br><strong>info@danemorrowfilms.example</strong></span>
  </div>

  <div class="field" style="left:480px;top:194px;width:266px">First Name *</div>
  <div class="field" style="left:758px;top:194px;width:269px">Last Name *</div>
  <div class="field" style="left:480px;top:243px;width:266px">Phone # (optional)</div>
  <div class="field" style="left:758px;top:243px;width:269px">Email Address *</div>
  <div class="field" style="left:480px;top:292px;width:266px">Wedding or Event Date *</div>
  <div class="field" style="left:758px;top:292px;width:269px">Ceremony &amp; Reception Venues</div>
  <div class="field" style="left:480px;top:327px;width:547px;height:72px;top:329px">Message *</div>
  <div class="submit">Submit</div>

  <p class="legal">Copyright © 2017 Dane Morrow Films. All Rights Reserved.<br>Terms of Use &nbsp;|&nbsp; Privacy &nbsp;|&nbsp; Sitemap</p>
  <div class="social"><span></span><span></span><span></span><span></span><span></span></div>
</section>

</div>
</body>
</html>
```